We need a range of stationery items designed for our active, community-orientated, out-going, all-age, family-friendly church in central Auckland, New Zealand.
We want to refresh and modernize the branding/images for Kereru Gospel Chapel itself so this image reflects who we are and our values.
Our church is located on a very busy intersection in the heart of a multi-ethnic local community. A number of churches and other groups use our site so we have branded our site as "The Meeting Pole". We have an existing logo for "The Meeting Pole" (see attached).
We would like you to design 4 items: a Letterhead, a With Compliments slip, a Business Card, and the Front Cover of our church newsletter, but we've included a request for an Email signature as an optional extra for this brief.
Organisation Details:
Name: Kereru Gospel Chapel
Postal Address: PO Box 38514, Wharenui, Auckland 1893
Email: office@kererugospel.org.nz
Phone: 09 473 5619
Web: www.kererugospel.org.nz (current website will be changed)
Position Statement: "a place of hope, belonging and worship"
Fonts:
The fonts for the "The Meeting Pole" logo are Futura Medium BT and Futura Lt BT. We would like the Futura font family used in the designs but feel free to add other fonts as appropriate (preferably True Type open source ones).
Colours:
Our current external signage colours are Dark Grey (Tolvar Coatings 'Slatewick' - RGB 57-55-53 ) and orange ( Tolvar 'Sunflare' - RGB 255-82-0 ). These are the colours for 'The Meeting Pole' which is our site. As we have other churches using our premises also we are looking to create a separate but complimentary identity for Kereru Gospel Chapel with a different colour set. We would ideally like a primary colour, a complimentary colour and an offset colour.
Design:
For the Kereru Gospel Chapel stationary we want the design to incorporate some of the elements of the 'Meeting Pole' particularly the extended 'T' device, so that we develop a separate identity but in the same family. We would like something that will look good for a number of years, rather than something that will date quickly in a year or two as fashions change.
PROJECTS
1. Letterhead
Finished size A4 (210 mm wide x 297mm tall)
This will become a template in MSWord. It will be printed in colour on our office photocopier so it must have a 5mm white border around the entire outside edge of the A4 page. "The Meeting Pole" logo needs to be incorporated in some form on the page.
2. With Compliments slip
Finished size 210 mm wide x 99 mm tall
This will be printed in colour on our office photocopier so it must have a 5mm white border around the entire outside edge of the slip. We will print these slips 3-up on an A4 page. The actual design space will be 200mm x 89mm. It is envisaged that this slip will use the same elements as the letterhead design. Please supply two versions, with and without the words "With Compliments".
3. Business Card
Finished size 90 mm wide by 55 mm tall.
This will be printed by commercial printers so colours can run to the edge of the card. Your Kereru Gospel Logo with the extended 'T' devise will need to feature on this.
4. Front Cover of Church Newsletter
Finished size 100 mm wide x 210 mm tall.
Our newsletter is printed in landscape on A4 paper and is folded twice.
It will be printed in colour on our office photocopier so it will need to have a minimum 5mm white border on all 4 sides. Attractive inviting colours preferred.
Needs to have:
- a place for the words Sunday and a date (which will change each Sunday)
- your Kereru Gospel Logo with the extended 'T' devise
- the words Sundays @ 10am
- the words ""a place of hope, belonging and worship"
- optional - "The Meeting Pole" logo (background does not need to be black)
5. Email Signature - optional extra
Not too large but something that will enable those receiving emails to instantly recognize who the email is from. Needs to include your Kereru Gospel logo, the name of the person, their position and our contact details.
Reason: We are extending the deadline on this project in order to encourage a broader range of designs, both from those who have already submitted designs and from those who are considering entering our competition. We'd love to see what you have to offer so please do submit your designs.
Re: Stationery for Kereru Gospel Chapel
Thanks to all the designers who have submitted designs for our competition so far. We have refrained from requesting a whole lot of tweaks to individual designs out of respect for your time as we understand that you are all busy professionals and that design competitions like this are just one way that you pitch for new business.
We would though like to offer some general comments on the submissions that we have seen so far. One thing that we would definitely like to arrive at via this process is to decide on a colour scheme. For this, as per the brief notes ( but possibly obscured by some of the other detail ) we want to have a primary colour and an offset colour and also an accent colour in the pallet.
Another thing that we maybe didn't make clear enough is that the colours for the identity of the site, known as The Meeting Pole, uses dark grey and orange but that we wanted to develop a separate but related identity for Kereru Gospel Chapel that meets there as we also now have other congregations that use our buildings.
One of the keys for the new identity will be the new colour pallet which we wanted to steer away from the darker tones that we used for the site branding. Therefore we would very much like to see your suggestions one or two secondary colours along with the primary brand colour if possible please.
Thank you all once again.
Kind regards

```html
<!DOCTYPE html>
<html lang="en">
<head>
<meta charset="utf-8">
<title>Kereru Gospel Chapel – Newsletter Cover</title>
<link href="https://fonts.googleapis.com/css2?family=Jost:wght@400;500&display=swap" rel="stylesheet">
<style>
  :root {
    --navy: #1f3d96;
    --teal: #3bbfc2;
    --charcoal: #323335;
    --white: #ffffff;
    --backdrop: #ffffff;
    --card-edge: #e4e4e4;
  }
  html, body {
    margin: 0;
    padding: 0;
    width: 1200px;
    height: 1000px;
    overflow: hidden;
    background: var(--backdrop);
    font-family: "Jost", "Futura", sans-serif;
  }
  .canvas {
    position: relative;
    width: 1200px;
    height: 1000px;
  }
  .cover {
    position: absolute;
    left: 396px;
    top: 66px;
    width: 408px;
    height: 868px;
    background: var(--white);
    outline: 1px solid var(--card-edge);
  }
  .masthead-frame {
    position: absolute;
    left: 20px;
    top: 20px;
    width: 368px;
    height: 190px;
  }
  .masthead {
    position: absolute;
    right: 38px;
    top: 42px;
    text-align: right;
    margin: 0;
  }
  .church-name {
    display: block;
    color: var(--navy);
    font-weight: 400;
    font-size: 40px;
    line-height: 44px;
    letter-spacing: 0.5px;
  }
  .publication {
    display: block;
    margin-top: 20px;
    color: var(--teal);
    font-weight: 400;
    font-size: 36px;
    line-height: 40px;
  }
  .feature-panel {
    position: absolute;
    left: 20px;
    top: 232px;
    width: 368px;
    height: 595px;
    background: var(--teal);
    color: var(--white);
  }
  .panel-text {
    position: absolute;
    right: 22px;
    text-align: right;
    margin: 0;
    font-weight: 400;
    font-size: 32px;
    line-height: 42px;
  }
  .issue-date { top: 42px; }
  .position-statement { top: 192px; }
  .service-time { top: 386px; }
  .site-mark {
    position: absolute;
    right: 22px;
    bottom: 22px;
    display: flex;
    align-items: center;
    gap: 10px;
    color: var(--white);
    font-weight: 400;
    font-size: 16px;
    letter-spacing: 1px;
    text-transform: uppercase;
  }
  .site-mark-square {
    width: 46px;
    height: 46px;
    background: var(--charcoal);
  }
  .footer-rule {
    position: absolute;
    left: 20px;
    top: 845px;
    width: 368px;
    height: 3px;
    background: var(--navy);
  }
</style>
</head>
<body>
<div class="canvas">
  <section class="cover">
    <svg class="masthead-frame" width="368" height="190" viewBox="0 0 368 190" aria-hidden="true">
      <polyline points="1.5,190 1.5,1.5 366.5,1.5 366.5,190" fill="none" stroke="var(--navy)" stroke-width="3"/>
    </svg>
    <h1 class="masthead">
      <span class="church-name">KERERU GOSPEL<br>CHAPEL</span>
      <span class="publication">NEWSLETTER</span>
    </h1>

    <div class="feature-panel">
      <p class="panel-text issue-date">Sunday 12th<br>November 2014</p>
      <p class="panel-text position-statement">A place of hope,<br>belonging and<br>worship.</p>
      <p class="panel-text service-time">Sundays @ 10 am</p>
      <div class="site-mark">
        <span class="site-mark-name">The Meeting Pole</span>
        <span class="site-mark-square"></span>
      </div>
    </div>

    <div class="footer-rule"></div>
  </section>
</div>
</body>
</html>
```